Grand Opening Banner needed for Marvelous Carpets and Home

My website is www.MarvelousCarpetsandHome.com (login with password 'plorka')

A full page banner 1000px X 500px with bright, lively colors and wording that shows an exciting GRAND OPENING celebration throughout the site. Banner needs to convey the following...

Grand Opening Sale
Runs through end of the month
Savings in every department
30 day Returns
Free Rug Pads with every rug
Free shipping.

Banner can be a simple background with graphics and text, or can be a room scene with rugs and furniture, or a grouping of rugs with text.

Some Ideas and Images can be taken from our vendor's websites, such as:

http://tbvendora.com/
http://dosmir.com/dosmir_2015/
http://www.pqmats.com/
http://zaverto.com/
http://shopbelwyn.com/

I also have quite a few room scene images available for use, if you desire.

Target Market(s)

Affluent women who care about stylish decor for their homes

Industry/Entity Type

Home And Garden

Requirements
Must have
• bold, vibrant appearance. Text that can be modified in Photoshop.
Nice to have
• HAND DRAWN, ARTIST STYLE ARTWORK IS GREATLY APPRECIATED.
• flat graphics and text with little to no 3 dimensional (shadow) effect. Font styles should be elegant/luxurious. An organic, scribbled, or painted style is nice in keeping with the handmade products that we sell.
• I am open to changing the color scheme of the website, to match your banner, so don't feel tied down to my existing colors.
Should not have
• nothing too modern or extreme in style.

```html
<!DOCTYPE html>
<html lang="en">
<head>
<meta charset="utf-8">
<title>Grand Opening Sale Banner</title>
<link rel="stylesheet" href="https://fonts.googleapis.com/css2?family=Cinzel:wght@500&family=Tenor+Sans&display=swap">
<style>
  :root {
    --page: #ffffff;
    --room-dark: #2a2220;
    --room-mid: #6b5b4f;
    --room-light: #b9ada0;
    --floor: #3a2018;
    --headline: #f7c81e;
    --sale-red: #c8141c;
    --sale-text: #ffffff;
    --label-bg: rgba(236, 232, 228, 0.82);
    --label-text: #1c1a18;
    --icon: #111111;
  }
  * { margin: 0; padding: 0; box-sizing: border-box; }
  html, body { width: 1200px; height: 1200px; overflow: hidden; background: var(--page); }
  .canvas { position: relative; width: 1200px; height: 1200px; background: var(--page); }
  .banner { position: absolute; left: 0; top: 0; width: 1200px; height: 600px; overflow: hidden; }
  .room-scene {
    position: absolute; inset: 0;
    background:
      linear-gradient(180deg, rgba(0,0,0,0) 0%, rgba(0,0,0,0) 62%, var(--floor) 82%, #241410 100%),
      linear-gradient(90deg, #c9c7c2 0%, var(--room-dark) 12%, #3b302b 30%, var(--room-mid) 45%, var(--room-light) 60%, #8e4a2c 72%, var(--room-light) 80%, #4d3e35 100%);
  }
  .sale-badge {
    position: absolute; left: 940px; top: 40px; width: 228px; height: 228px;
    border-radius: 50%; background: var(--sale-red); opacity: 0.92;
  }
  .sale-badge span {
    position: absolute; left: 50%; top: 50%;
    transform: translate(-50%, -62%) rotate(-28deg);
    font-family: "Cinzel", serif; font-size: 62px; color: var(--sale-text); letter-spacing: 3px;
  }
  .headline {
    position: absolute; left: 118px; top: 236px; width: 960px;
    font-family: "Cinzel", serif; font-weight: 500; font-size: 92px; line-height: 1;
    color: var(--headline); letter-spacing: 2px; white-space: nowrap;
    text-shadow: 0 2px 4px rgba(0,0,0,0.35);
  }
  .perk { position: absolute; display: flex; align-items: center; height: 40px; }
  .perk svg { width: 30px; height: 30px; margin-right: 24px; }
  .perk .label {
    height: 40px; line-height: 40px; padding: 0 12px;
    background: var(--label-bg); color: var(--label-text);
    font-family: "Tenor Sans", sans-serif; font-size: 27px; white-space: nowrap;
  }
  .perk-month { left: 164px; top: 396px; }
  .perk-pads { left: 164px; top: 456px; }
  .perk-savings { left: 164px; top: 518px; }
  .perk-returns { left: 764px; top: 396px; }
  .perk-shipping { left: 764px; top: 456px; }
</style>
</head>
<body>
<div class="canvas">
  <section class="banner">
    <div class="room-scene" role="img" aria-label="Photo of an elegant living room with a fireplace, wall-mounted TV, leather and linen sofas, a patterned red area rug and tall windows with rust curtains"></div>
    <div class="sale-badge"><span>SALE</span></div>
    <h1 class="headline">GRAND OPENING</h1>

    <div class="perk perk-month">
      <svg viewBox="0 0 30 30"><rect x="5" y="5" width="20" height="20" fill="var(--icon)" transform="rotate(45 15 15)"/><rect x="11" y="11" width="8" height="8" fill="#fff"/></svg>
      <span class="label">Runs through end of the month</span>
    </div>
    <div class="perk perk-pads">
      <svg viewBox="0 0 30 30"><rect x="5" y="5" width="20" height="20" fill="var(--icon)" transform="rotate(45 15 15)"/><rect x="11" y="11" width="8" height="8" fill="#fff"/></svg>
      <span class="label">Free rug pads with every rug</span>
    </div>
    <div class="perk perk-savings">
      <svg viewBox="0 0 30 30"><rect x="5" y="5" width="20" height="20" fill="var(--icon)" transform="rotate(45 15 15)"/><rect x="11" y="11" width="8" height="8" fill="#fff"/></svg>
      <span class="label">Savings in every department</span>
    </div>
    <div class="perk perk-returns">
      <svg viewBox="0 0 30 30"><rect x="5" y="5" width="20" height="20" fill="var(--icon)" transform="rotate(45 15 15)"/><rect x="11" y="11" width="8" height="8" fill="#fff"/></svg>
      <span class="label">30 day returns</span>
    </div>
    <div class="perk perk-shipping">
      <svg viewBox="0 0 30 30"><rect x="5" y="5" width="20" height="20" fill="var(--icon)" transform="rotate(45 15 15)"/><rect x="11" y="11" width="8" height="8" fill="#fff"/></svg>
      <span class="label">Free shipping</span>
    </div>
  </section>
</div>
</body>
</html>
```